Brookvale Services telephone book advert

Design a tellwick directory telephone book advertisement. Attached is a current version of the brookvale services advert. Please use the same information as detailed on the existing advert but arty!. Overall size should be 130 mm by 91 mm portrait using one of the specified colours plus black. Any background should be opaque (not white). and delivered in the formats as specified.

```html
<!DOCTYPE html>
<html lang="en">
<head>
<meta charset="utf-8">
<title>Brookvale Services – Tellwick Directory Advert</title>
<link href="https://fonts.googleapis.com/css2?family=Montserrat:ital,wght@0,700;0,800;0,900;1,500&family=Didact+Gothic&display=swap" rel="stylesheet">
<style>
  :root {
    --page: #ffffff;
    --brand-blue: #1b6ebe;
    --ink: #0b0b0b;
    --white: #ffffff;
    --deep: #0d1f3a;
  }
  * { margin: 0; padding: 0; box-sizing: border-box; }
  html, body {
    width: 1200px; height: 848px; overflow: hidden;
    background: var(--page);
  }
  .advert {
    position: absolute; left: 410px; top: 174px;
    width: 366px; height: 523px;
    background: var(--brand-blue);
    color: var(--white);
    font-family: "Didact Gothic", "Helvetica Neue", Arial, sans-serif;
    overflow: hidden;
  }
  .abs { position: absolute; }
  .company-name {
    left: 16px; top: 18px;
    font-family: "Montserrat", Arial, sans-serif;
    font-weight: 800; font-size: 24px; line-height: 30px;
    letter-spacing: 0.5px; text-transform: uppercase;
  }
  .company-suffix {
    left: 16px; top: 82px; font-size: 18px;
  }
  .speech-bubble { left: 0; top: 0; }
  .bubble-text {
    left: 219px; top: 20px; font-size: 15px; line-height: 17px;
  }
  .phone-number {
    left: 14px; top: 112px;
    font-family: "Montserrat", Arial, sans-serif;
    font-weight: 900; font-size: 72px; line-height: 90px;
    letter-spacing: -1px; white-space: nowrap;
    text-shadow: 4px 4px 0 var(--ink);
  }
  .service-tag {
    left: 0; width: 132px; height: 21px;
    background: var(--ink);
    clip-path: polygon(0 0, 100% 0, calc(100% - 12px) 100%, 0 100%);
    font-family: "Montserrat", Arial, sans-serif;
    font-style: italic; font-weight: 500; font-size: 13px; line-height: 21px;
    padding-left: 17px; white-space: nowrap;
  }
  .service-detail {
    left: 37px; font-size: 13.5px; line-height: 17px;
  }
  .service-detail.indented { left: 40px; }
  .info-column { left: 196px; }
  .home-surveys {
    top: 199px; color: var(--deep); font-size: 16px; line-height: 17px;
  }
  .info-line { font-size: 13.5px; line-height: 17px; }
  .info-line svg { vertical-align: -1px; margin-right: 6px; }
  .manager-name {
    top: 263px; font-family: "Montserrat", Arial, sans-serif;
    font-weight: 700; font-size: 17px;
  }
  .website {
    top: 405px; font-family: "Montserrat", Arial, sans-serif;
    font-weight: 700; font-size: 17px;
  }
  .divider { top: 434px; width: 100px; height: 2px; background: var(--white); }
  .address { top: 444px; font-size: 13.5px; line-height: 17px; }
</style>
</head>
<body>
  <article class="advert">
    <h1 class="abs company-name">Brookvale<br>Services</h1>
    <p class="abs company-suffix">Limited</p>

    <svg class="abs speech-bubble" width="366" height="120" viewBox="0 0 366 120" aria-hidden="true">
      <polyline points="198,0 198,95 318,95 366,52" fill="none" stroke="var(--white)" stroke-width="2.5"/>
    </svg>
    <p class="abs bubble-text">For local<br>brookvale<br>expertise<br>call:</p>

    <p class="abs phone-number">318 - 462</p>

    <div class="abs service-tag" style="top:202px">Emergencies</div>
    <p class="abs service-detail" style="top:224px">Unblocking &amp; high<br>pressure cleaning</p>

    <div class="abs service-tag" style="top:277px">Maintenance</div>
    <p class="abs service-detail" style="top:299px">Jetting, de-scaling<br>&amp; root cutting</p>

    <div class="abs service-tag" style="top:349px">Rehabilitation</div>
    <p class="abs service-detail indented" style="top:371px">Structural re-lining<br>of damaged and<br>leaky drains</p>

    <div class="abs service-tag" style="top:439px">Survey</div>
    <p class="abs service-detail" style="top:461px">Unblocking &amp; high<br>pressure cleaning</p>

    <p class="abs info-column home-surveys">Home Buyer<br>Surveys</p>
    <p class="abs info-column info-line" style="top:245px"><svg width="10" height="10" viewBox="0 0 10 10" aria-hidden="true"><polygon points="0,0 10,0 0,10" fill="var(--ink)"/></svg>Contracts Manager</p>
    <p class="abs info-column manager-name">Owen Farrant</p>
    <p class="abs info-column info-line" style="top:302px"><svg width="10" height="10" viewBox="0 0 10 10" aria-hidden="true"><polygon points="0,0 10,0 0,10" fill="var(--ink)"/></svg>email: office@bvs.gg</p>
    <p class="abs info-column info-line" style="top:335px"><svg width="10" height="10" viewBox="0 0 10 10" aria-hidden="true"><polygon points="0,0 10,0 0,10" fill="var(--ink)"/></svg> For more<br>information please<br>visit our website:</p>
    <p class="abs info-column website">www.bvs.gg</p>
    <div class="abs info-column divider"></div>
    <p class="abs info-column address">Carrow Lane<br>Road, St. Aldric,<br>Brookvale BV3 7KP</p>
  </article>
</body>
</html>
```